Summer Music/Chorus/Choir Camp for Young Singers Ages 8-13

We need a flyer for a summer camp for young singers ages 8-13. We are nonprofit community children's chorus in Miami, FL. Our camp provides specialized training in music theory, sight-reading,and aural training through daily choral rehearsals in an environment that is both positive and a lot of fun! Our camp offers children the opportunity to come as they are, no matter the level of experience, and grow tremendously in their musicianship skills. In addition to this, our campers participate in song-writing, masterclasses, community performances, and media projects. The final design should be clean, fun, not too crowded, should appeal to boys and girls ages 8-13, and something someone that age would consider "cool" and not too childish. Drawings are cool, something different.
Updates

Target Market(s)

Ages 8-13 and parents of those kids.

Industry/Entity Type

Community

Requirements
Must have
• All info attached.
Nice to have
• Things that relate to music, especially related to singing/choirs
Should not have
• instruments, stock photos of children, or photos from our website (unless they are used very creatively), or photos in general. I've attached our previous camp flyer and our current organization flyer but I don't necessarily want this flyer to look like those.

```html
<!DOCTYPE html>
<html lang="en">
<head>
<meta charset="utf-8">
<title>Summer Choral Camp</title>
<link href="https://fonts.googleapis.com/css2?family=Bowlby+One&family=Barlow+Semi+Condensed:ital,wght@0,400;0,500;0,600;0,700;0,800;1,500&display=swap" rel="stylesheet">
<style>
  :root {
    --orange: #f26a10;
    --orange-deep: #d9540a;
    --orange-light: #f9a13a;
    --ink: #111111;
    --paper: #f3f3f1;
    --white: #ffffff;
  }
  * { margin: 0; padding: 0; box-sizing: border-box; }
  html, body { width: 927px; height: 1200px; overflow: hidden; }
  body {
    background: radial-gradient(ellipse at 50% 40%, #fafaf8 0%, var(--paper) 70%, #e9e9e6 100%);
    font-family: "Barlow Semi Condensed", sans-serif;
    color: var(--ink);
  }
  .flyer { position: relative; width: 927px; height: 1200px; overflow: hidden; }

  .sun-mic-art {
    position: absolute; left: 227px; top: 0; width: 470px; height: 350px;
  }
  .headline { position: absolute; left: 60px; top: 270px; width: 810px; height: 260px; }
  .headline text { font-family: "Bowlby One", sans-serif; }

  .camp-banner {
    position: absolute; left: 295px; top: 482px; width: 334px; height: 68px;
    background: var(--orange); color: var(--white);
    font-family: "Barlow Semi Condensed", sans-serif; font-weight: 800;
    font-size: 44px; letter-spacing: 1px; line-height: 68px; text-align: center;
    box-shadow: 3px 3px 0 var(--orange-deep);
  }
  .star { position: absolute; width: 30px; height: 30px; fill: var(--orange); }

  .intro {
    position: absolute; left: 150px; top: 585px; width: 630px;
    font-size: 14.5px; font-weight: 500; line-height: 1.45;
    transform: rotate(-3deg); transform-origin: center;
  }

  .price { position: absolute; left: 0; top: 683px; width: 927px; text-align: center; }
  .price-amount { font-size: 38px; font-weight: 700; color: var(--orange); line-height: 1; }
  .price-session { font-size: 42px; font-weight: 800; line-height: 1.05; }
  .price-note { font-size: 15px; font-weight: 500; }

  .dots { position: absolute; height: 4px;
    background-image: radial-gradient(circle, var(--ink) 1.8px, transparent 2px);
    background-size: 11px 4px; }
  .label { color: var(--orange); font-weight: 700; font-size: 23px; letter-spacing: 3px; }

  .venue { position: absolute; right: 440px; top: 825px; text-align: right; }
  .venue .label { display: block; line-height: 1.1; }
  .venue p { font-size: 20px; font-weight: 500; line-height: 1.3; }

  .divider { position: absolute; left: 520px; top: 818px; width: 2px; height: 100px; background: var(--ink); }

  .date { position: absolute; left: 535px; top: 830px; }
  .date .label { display: block; line-height: 1.1; }
  .date-main { font-size: 20px; font-weight: 500; line-height: 1.2; }
  .date-extra { font-size: 12.5px; font-weight: 500; line-height: 1.25; width: 240px; }

  .partners { position: absolute; left: 190px; top: 962px; width: 560px; height: 70px; display: flex; align-items: center; gap: 14px; }
  .partner-name { font-weight: 700; font-size: 15px; color: var(--ink); display: flex; align-items: center; gap: 6px; }
  .partner-name.chorus { font-size: 16px; width: 150px; line-height: 1.05; }
  .partner-dot { width: 14px; height: 14px; border-radius: 50%; background: var(--ink); flex: none; }
  .partner-badge { width: 64px; height: 64px; border: 3px solid var(--ink); background: var(--white); flex: none; }

  .contact-title { position: absolute; left: 0; top: 1054px; width: 927px; text-align: center; font-size: 21px; font-weight: 700; }
  .contact-row { position: absolute; left: 0; top: 1088px; width: 927px; height: 48px; }
  .contact-web { position: absolute; left: 33px; top: 10px; font-size: 20px; font-weight: 500; }
  .contact-phone {
    position: absolute; left: 364px; top: 0; width: 215px; height: 48px;
    background: var(--orange); color: var(--white); text-align: center;
    font-size: 20px; font-weight: 500; line-height: 48px;
  }
  .contact-mail { position: absolute; left: 601px; top: 10px; font-size: 20px; font-weight: 500; }

  .edge-letter { position: absolute; left: 882px; top: 1030px; font-family: "Barlow Semi Condensed", sans-serif; font-weight: 800; font-size: 58px; color: var(--orange); line-height: 1; }

  .legal { position: absolute; left: 0; top: 1162px; width: 927px; text-align: center; font-size: 12.5px; font-weight: 500; }
</style>
</head>
<body>
<main class="flyer">

  <svg class="sun-mic-art" viewBox="0 0 470 350" role="img" aria-label="Illustration of a vintage microphone under a rising orange sun with rays">
    <defs>
      <radialGradient id="sunGlow" cx="50%" cy="75%" r="60%">
        <stop offset="0%" stop-color="#f9a13a"/>
        <stop offset="100%" stop-color="#f26a10"/>
      </radialGradient>
    </defs>
    <path d="M20 340 A215 215 0 0 1 450 340 L420 340 A185 185 0 0 0 50 340 Z" fill="url(#sunGlow)"/>
    <ellipse cx="235" cy="250" rx="70" ry="110" fill="#d8d8d4" opacity="0.6"/>
  </svg>

  <svg class="headline" viewBox="0 0 810 260" aria-label="Summer">
    <defs>
      <path id="arc" d="M20 235 Q405 40 790 235"/>
      <linearGradient id="letterFill" x1="0" y1="0" x2="0" y2="1">
        <stop offset="0%" stop-color="#f9a13a"/>
        <stop offset="100%" stop-color="#f26a10"/>
      </linearGradient>
    </defs>
    <text font-size="150" fill="#b8470a" transform="translate(6,8)"><textPath href="#arc" startOffset="50%" text-anchor="middle" textLength="800">SUMMER</textPath></text>
    <text font-size="150" fill="url(#letterFill)"><textPath href="#arc" startOffset="50%" text-anchor="middle" textLength="800">SUMMER</textPath></text>
  </svg>

  <svg class="star" style="left:205px;top:522px" viewBox="0 0 24 24"><path d="M12 1l3.2 7 7.6.8-5.7 5.1 1.6 7.5L12 17.6 5.3 21.4l1.6-7.5L1.2 8.8 8.8 8z"/></svg>
  <svg class="star" style="left:245px;top:530px" viewBox="0 0 24 24"><path d="M12 1l3.2 7 7.6.8-5.7 5.1 1.6 7.5L12 17.6 5.3 21.4l1.6-7.5L1.2 8.8 8.8 8z"/></svg>
  <svg class="star" style="left:645px;top:505px" viewBox="0 0 24 24"><path d="M12 1l3.2 7 7.6.8-5.7 5.1 1.6 7.5L12 17.6 5.3 21.4l1.6-7.5L1.2 8.8 8.8 8z"/></svg>
  <svg class="star" style="left:688px;top:512px" viewBox="0 0 24 24"><path d="M12 1l3.2 7 7.6.8-5.7 5.1 1.6 7.5L12 17.6 5.3 21.4l1.6-7.5L1.2 8.8 8.8 8z"/></svg>

  <div class="camp-banner">CHORAL CAMP</div>

  <p class="intro">"Youth and children who love to sing will have a blast at our choral camp! Our music educators and industry professionals are dedicated to enhancing the lives of young singers through choral training which develops vocal technique, ear-training, music reading, and interpersonal skills. Activities are fun and interactive and former music training is not necessary. Singers in grades 3-9 are invited to attend! Register today!</p>

  <section class="price">
    <div class="price-amount">Cost : $300</div>
    <div class="price-session">for 2-week session</div>
    <div class="price-note">Price does not include lunch.</div>
  </section>

  <div class="dots" style="left:198px;top:845px;width:180px"></div>
  <section class="venue">
    <span class="label">VENUE</span>
    <p>Southgate<br>Cultural Arts Center, 4820 SW 180th<br>Street Miami, FL 33187.</p>
  </section>

  <div class="divider"></div>

  <div class="dots" style="left:618px;top:820px;width:120px"></div>
  <section class="date">
    <span class="label">DATE</span>
    <div class="date-main">July 18-29&nbsp; 9am-3pm (M-F)</div>
    <div class="date-extra">Extended hours available (7:30am-5:30pm) for an extra $50 per week.</div>
  </section>

  <section class="partners">
    <div class="partner-name chorus"><span class="partner-dot"></span>Bright Harmony Chorus</div>
    <div class="partner-badge"></div>
    <div class="partner-name">Coral Bay County</div>
    <div class="partner-name"><span class="partner-dot"></span>Lantern Foundation</div>
  </section>

  <h2 class="contact-title">Our Contact information</h2>
  <section class="contact-row">
    <span class="contact-web">www.brightharmonychorus.org</span>
    <span class="contact-phone">786.555.0148</span>
    <span class="contact-mail">hello@brightharmonychorus.org</span>
  </section>

  <span class="edge-letter">W</span>

  <p class="legal">"Bright Harmony Chorus is a 501 (c)(3) Nonprofit organization. Donations made to BHC are tax-exempt."</p>
</main>
</body>
</html>
```